Brindlecove Flood Restoration needing website

Hi Team

We are looking for a 4 or 5 page website containing
1: Home
2: Services
3: Gallery
4: Equipment Hire
5 Contact Us

Would want the front page to be a big call to action. Someones house has just flooded...they're highly stressed and we just want to let them know straight away that we can assist them

Some call to action would be great.

"Wet Carpets??"

"Washing machine just overflowed??"

"Burst pipe?"

"We're here to help!!"

Would be wanting a scrolling banner type homepage with images of flooded houses, heavy rain, a mother in shock that the house has been flooded by an overflowing washing machine, someone taking an emergency call with text saying that we are there to take your call 24/7 365 days a year

Target Market(s)

insurance companies and home owners

Industry/Entity Type

Hire

Coding

Coded - Design and coding required

Number of Pages Required

5+ page

Requirements
Must have
• 24/7 emergency contact number on home page (0498215763)
• 4 photos on banner on home page
• Equipment Hire Page should include images and brief description of these 3 products
• http://www.ptkdirect.example.com.au/prod458.htm
• http://www.gustline-gear.example.com.au/product/mistral-breeze-fan/
• http://www.vendrasuck.example.com.au/carpet/carpet-extractor-harrier-xv-x-vi-x-vii
• SERVICES OFFERED ARE:
• 24/7 Emergnecy Flood Restoration
• Insurance Claims
• Structural Drying
• Sub Floor Drying
• Supply and installation of drying equipment
• Professional Carpet and underlay installation
Nice to have
• Some other websites we like
• www.kelbyleakfixers.example.com.au
• www.summitrecoverywashing.example.com.au/flood-water-damage-restoration
• http://www.pelhamrecovery.example.com.au/
• http://www.dampfixnational.example.com.au/
Should not have
• not looking for an all white background.

```html
<!DOCTYPE html>
<html lang="en">
<head>
<meta charset="utf-8">
<title>Brindlecove Flood Restoration</title>
<link href="https://fonts.googleapis.com/css2?family=Montserrat:wght@400;500;600;700&family=Open+Sans:wght@400;600;700&family=Oswald:wght@400&display=swap" rel="stylesheet">
<style>
:root{
  --blue:#2a95d2;
  --ink:#2b2b2b;
  --text:#444;
  --white:#fff;
  --footer:#242424;
  --footer-bottom:#1b1b1b;
  --panel:#f2f2f2;
  --fb:#3b5a98;
  --tw:#3ea9de;
  --li:#1278b1;
  --gp:#dc4a38;
}
*{box-sizing:border-box;margin:0;padding:0}
html,body{width:1200px;height:2624px;overflow:hidden}
body{font-family:"Open Sans",Arial,sans-serif;color:var(--text);background:var(--white);position:relative}

/* header */
.site-header{position:absolute;left:0;top:0;width:1200px;height:105px;background:#f7f8f9}
.brand{position:absolute;left:100px;top:26px;display:flex;align-items:center;gap:12px}
.brand-mark{width:34px;height:34px;border-radius:50%;background:var(--blue)}
.brand-name{font-family:"Montserrat",sans-serif;font-weight:700;font-size:19px;color:var(--blue);line-height:1.15;width:230px}
.emergency{position:absolute;left:727px;top:12px;display:flex;align-items:center;gap:12px}
.emergency-icon{width:40px;height:40px;border-radius:50%;background:var(--blue);display:flex;align-items:center;justify-content:center}
.emergency-label{font-size:12px;color:#666}
.emergency-number{font-family:"Montserrat",sans-serif;font-size:22px;font-weight:600;color:var(--blue);line-height:1}
.social{position:absolute;display:flex;gap:7px}
.social-dot{width:28px;height:28px;border-radius:50%;display:block}
.s1{background:var(--fb)}.s2{background:var(--tw)}.s3{background:var(--li)}.s4{background:var(--gp)}
.main-nav{position:absolute;top:70px;left:553px;display:flex;font-family:"Montserrat",sans-serif;font-size:13px;color:#444}
.main-nav a{text-decoration:none;color:inherit}
.main-nav .active{color:var(--blue)}

/* hero */
.hero{position:absolute;left:0;top:105px;width:1200px;height:485px;background:linear-gradient(100deg,#4e6872 0%,#6e8a8c 35%,#a6b9b3 55%,#7f9a9c 75%,#4f676b 100%)}
.hero-floor{position:absolute;left:0;bottom:0;width:100%;height:150px;background:linear-gradient(180deg,rgba(70,170,180,0),rgba(60,160,175,.55))}
.hero-line1{position:absolute;left:100px;top:196px;background:#111;color:#fff;font-family:"Oswald",sans-serif;font-size:27px;padding:4px 12px;line-height:1.2}
.hero-line2{position:absolute;left:100px;top:244px;background:var(--blue);color:#fff;font-family:"Oswald",sans-serif;font-size:25px;padding:2px 12px}
.hero-btn{position:absolute;left:100px;top:303px;width:132px;height:37px;background:#fff;color:#111;font-family:"Montserrat",sans-serif;font-weight:600;font-size:12px;display:flex;align-items:center;justify-content:center}
.hero-arrow{position:absolute;top:223px;width:47px;height:38px;background:rgba(255,255,255,.75);display:flex;align-items:center;justify-content:center}

/* headings */
.section-title{position:absolute;left:0;width:1200px;text-align:center;font-family:"Montserrat",sans-serif;font-weight:500;font-size:29px;color:var(--ink)}
.section-title em{font-style:normal;color:var(--blue)}
.title-rule{position:absolute;left:562px;width:76px;height:5px;border-top:1px solid #888;border-bottom:1px solid #888}

/* welcome */
.welcome-text{position:absolute;left:100px;top:704px;width:1000px;text-align:center;font-size:12.4px;line-height:27px;color:#444}
.btn{position:absolute;height:37px;font-family:"Montserrat",sans-serif;font-size:12px;font-weight:600;display:flex;align-items:center;justify-content:center}
.btn-blue{background:var(--blue);color:#fff}
.btn-line{border:1px solid #555;color:#222;background:#fff}

/* services */
.services{position:absolute;left:0;top:925px;width:1200px;height:499px;background:linear-gradient(180deg,#3d9fd6 0%,#3b98cf 60%,#3a93c8 100%)}
.services-shade{position:absolute;inset:0;background:linear-gradient(90deg,rgba(255,255,255,.06),rgba(0,40,80,.12) 50%,rgba(255,255,255,.05))}
.services .section-title{color:#fff;top:36px}
.services .title-rule{border-color:#e6f2fa;top:84px}
.service{position:absolute;width:270px;color:#fff}
.service h3{font-family:"Montserrat",sans-serif;font-size:15px;font-weight:600;margin-bottom:8px}
.service p{font-size:11.6px;font-weight:600;line-height:18px}
.service.right{text-align:right}
.service-icon{position:absolute;width:56px;height:56px}
.btn-white{background:#fff;color:#222}

/* gallery */
.gallery-panel{position:absolute;left:100px;top:1562px;width:1000px;height:428px;background:var(--panel)}
.photo{position:absolute;border:2px solid #e7e2da}
.ph1{left:118px;top:1582px;width:305px;height:183px;background:linear-gradient(135deg,#8a6a45,#c8a55e 40%,#3e7fa8 70%,#7a5a38)}
.ph2{left:446px;top:1582px;width:305px;height:183px;background:linear-gradient(180deg,#a9c2d8 0%,#c9d5de 40%,#6d5e44 60%,#8b7452 100%)}
.ph3{left:775px;top:1582px;width:305px;height:390px;background:linear-gradient(160deg,#e9e4dc 0%,#d7cfc3 35%,#4f86b5 55%,#2f5f8e 75%,#c7a77b 100%)}
.ph4{left:118px;top:1785px;width:305px;height:187px;background:linear-gradient(120deg,#c9b07a,#e2d7c0 35%,#4c5a70 60%,#caa55a)}
.ph5{left:446px;top:1785px;width:305px;height:187px;background:linear-gradient(135deg,#ece9e3,#f5f3ee 50%,#e2ddd2);border:5px solid #4a463d}

/* contact */
.contact{position:absolute;left:0;top:2050px;width:1200px;height:252px;background:linear-gradient(90deg,#ecebe8,#e4e2dd 50%,#d9d6cf)}
.contact h2{position:absolute;left:100px;top:40px;font-family:"Montserrat",sans-serif;font-size:29px;font-weight:500;color:#222;line-height:38px}
.contact p{position:absolute;left:100px;top:127px;width:310px;font-size:12.4px;line-height:20px;color:#444}
.field{position:absolute;height:42px;background:#fff;font-size:12.4px;color:#555;padding:13px 14px}
.submit{position:absolute;left:458px;top:2220px;width:154px;height:42px;background:#111;color:#fff;font-family:"Montserrat",sans-serif;font-weight:700;font-size:15px;display:flex;align-items:center;justify-content:center}

/* footer */
.site-footer{position:absolute;left:0;top:2302px;width:1200px;height:270px;background:var(--footer);color:#d4d4d4}
.foot-col{position:absolute;top:36px}
.foot-col h4{font-family:"Montserrat",sans-serif;font-size:17px;font-weight:600;color:#fff;padding-bottom:9px;border-bottom:1px solid #555;margin-bottom:14px}
.foot-links li{list-style:none;font-size:12px;line-height:31px}
.contact-list li{list-style:none;font-size:12px;display:flex;gap:14px;align-items:flex-start;margin-bottom:13px;line-height:18px}
.contact-list svg{flex:none;margin-top:2px}
.map{position:absolute;left:532px;top:2397px;width:272px;height:139px;background:linear-gradient(135deg,#c8dcb8,#e8e4d6 40%,#a8cce0 60%,#dfe6cf)}
.copy-bar{position:absolute;left:0;top:2572px;width:1200px;height:52px;background:var(--footer-bottom)}
.copy-text{position:absolute;left:100px;top:17px;font-size:12px;color:#ccc}
</style>
</head>
<body>

<header class="site-header">
  <div class="brand"><span class="brand-mark"></span><span class="brand-name">Brindlecove Flood Restoration</span></div>
  <div class="emergency">
    <span class="emergency-icon"><svg width="20" height="20" viewBox="0 0 24 24"><path fill="#fff" d="M6.6 10.8a15 15 0 0 0 6.6 6.6l2.2-2.2c.3-.3.7-.4 1-.2 1.1.4 2.3.6 3.6.6.6 0 1 .4 1 1V20c0 .6-.4 1-1 1A17 17 0 0 1 3 4c0-.6.4-1 1-1h3.5c.6 0 1 .4 1 1 0 1.3.2 2.5.6 3.6.1.3 0 .7-.2 1z"/></svg></span>
    <div><div class="emergency-label">24/7 Emergency Number</div><div class="emergency-number">0498 215 763</div></div>
  </div>
  <div class="social" style="left:962px;top:20px"><span class="social-dot s1"></span><span class="social-dot s2"></span><span class="social-dot s3"></span><span class="social-dot s4"></span></div>
  <nav class="main-nav">
    <a class="active" style="width:98px">Home</a><a style="width:113px">Services</a><a style="width:105px">Gallery</a><a style="width:155px">Equipment Hire</a><a>Contact Us</a>
  </nav>
</header>

<section class="hero" role="img" aria-label="Woman in a laundry room flooded by an overflowing washing machine">
  <div class="hero-floor"></div>
  <div class="hero-arrow" style="left:0"><svg width="22" height="10" viewBox="0 0 22 10"><path d="M22 5H2M6 1 2 5l4 4" stroke="#333" fill="none" stroke-width="1.4"/></svg></div>
  <div class="hero-arrow" style="right:0"><svg width="22" height="10" viewBox="0 0 22 10"><path d="M0 5h20M16 1l4 4-4 4" stroke="#333" fill="none" stroke-width="1.4"/></svg></div>
  <div class="hero-line1">"Washing machine just overflowed??"</div>
  <div class="hero-line2">We can Help</div>
  <div class="hero-btn">CONTACT NOW!</div>
</section>

<h1 class="section-title" style="top:640px">Welcome To <em>Brindlecove Restorations</em></h1>
<div class="title-rule" style="top:687px"></div>
<p class="welcome-text">Lorem ipsum dolor sit amet, consectetuer adipiscing elit, sed diam nonummy nibh euismod tincidunt ut laoreet dolore magna aliquam erat volutpat. Ut wisi enim ad minim veniam, quis nostrud exerci tation ullamcorper suscipit lobortis nisl ut aliquip ex ea commodo consequat. Duis autem vel eum iriure dolor in hendrerit in vulputate velit esse molestie consequat, vel illum dolore eu feugiat nulla facilisis at vero eros et accumsan et iusto odio dignissim qui blandit praesent luptatum zzril delenit augue duis dolore te feugait nulla facilisi.</p>
<div class="btn btn-blue" style="left:476px;top:832px;width:124px">READ MORE</div>
<div class="btn btn-line" style="left:608px;top:832px;width:135px">CONTACT NOW!</div>

<section class="services" role="img" aria-label="Flooded street of houses behind a blue overlay">
  <div class="services-shade"></div>
  <h2 class="section-title">Our Services</h2>
  <div class="title-rule"></div>

  <svg class="service-icon" style="left:100px;top:160px" viewBox="0 0 56 56"><circle cx="28" cy="28" r="22" fill="none" stroke="#fff" stroke-width="4"/><text x="28" y="34" text-anchor="middle" font-family="Montserrat,sans-serif" font-weight="700" font-size="17" fill="#fff">24</text></svg>
  <div class="service" style="left:189px;top:152px"><h3>24/7 FLOOD RESTORATION</h3><p>Accumsan et iusto odio dignissim quiosn blandit mori praesent luptatum zzril delenit augue duis dolore ten feugait facilisi...[+]</p></div>

  <svg class="service-icon" style="left:104px;top:290px" viewBox="0 0 56 56"><rect x="6" y="14" width="30" height="18" rx="9" fill="#fff"/><rect x="22" y="30" width="8" height="16" fill="#fff"/><path d="M40 16h12M40 23h12M40 30h12" stroke="#fff" stroke-width="3"/></svg>
  <div class="service" style="left:189px;top:280px"><h3>SUB FLOOR DRYING</h3><p>Accumsan et iusto odio dignissim quiosn blandit mori praesent luptatum zzril delenit augue duis dolore ten feugait facilisi...[+]</p></div>

  <div class="service right" style="left:736px;top:152px"><h3>STRUCTURAL DRYING</h3><p>Accumsan et iusto odio dignissim quiosn blandit mori praesent luptatum zzril delenit augue duis dolore ten feugait facilisi...[+]</p></div>
  <svg class="service-icon" style="left:1030px;top:146px" viewBox="0 0 56 56"><circle cx="20" cy="12" r="6" fill="#fff"/><circle cx="36" cy="14" r="5" fill="#fff"/><path d="M12 50 16 22h10l4 28M30 50l3-24h8l3 24" fill="#fff"/><path d="M44 20 52 6" stroke="#fff" stroke-width="3"/></svg>

  <div class="service right" style="left:736px;top:280px"><h3>Insurance Reporting</h3><p>Accumsan et iusto odio dignissim quiosn blandit mori praesent luptatum zzril delenit augue duis dolore ten feugait facilisi...[+]</p></div>
  <svg class="service-icon" style="left:1032px;top:284px" viewBox="0 0 56 56"><rect x="8" y="8" width="32" height="42" rx="3" fill="none" stroke="#fff" stroke-width="3"/><path d="M15 20h18M15 28h18M15 36h10" stroke="#fff" stroke-width="3"/><circle cx="42" cy="42" r="11" fill="#fff"/><path d="M37 42l4 4 6-7" stroke="#3a97cf" stroke-width="3" fill="none"/></svg>

  <div class="btn btn-white" style="left:508px;top:413px;width:184px">VIEW ALL SERVICES&nbsp;&nbsp;&nbsp;<svg width="20" height="10" viewBox="0 0 20 10"><path d="M0 5h18M14 1l4 4-4 4" stroke="#222" stroke-width="2" fill="none"/></svg></div>
</section>

<h2 class="section-title" style="top:1477px">Our <em>Gallery</em></h2>
<div class="title-rule" style="top:1524px"></div>
<div class="gallery-panel"></div>
<div class="photo ph1" role="img" aria-label="Drying hoses and air movers laid across a wet floor"></div>
<div class="photo ph2" role="img" aria-label="Timber-framed house standing in flood water"></div>
<div class="photo ph3" role="img" aria-label="Blue air mover fan on a room floor"></div>
<div class="photo ph4" role="img" aria-label="Drying equipment set up inside a damaged room"></div>
<div class="photo ph5" role="img" aria-label="Room interior with zoom overlay">
  <svg style="position:absolute;left:120px;top:60px" width="60" height="60" viewBox="0 0 60 60"><circle cx="24" cy="24" r="17" fill="none" stroke="#333" stroke-width="3"/><path d="M36 36l16 16M24 16v16M16 24h16" stroke="#333" stroke-width="3"/></svg>
</div>

<section class="contact" role="img" aria-label="Faded bright living room">
  <h2>Any Questions you<br>would like to ask?</h2>
  <p>Duis autem vel eum iriure dolormi opl inmoklmort hendi rerit in vulpu tateml velitm essemol monop molestiel conseqb uat, velmi illum dolor eokf nol atn nulla more facilisis... [+]</p>
</section>
<div class="field" style="left:458px;top:2117px;width:309px">Name</div>
<div class="field" style="left:793px;top:2117px;width:307px">Email</div>
<div class="field" style="left:458px;top:2168px;width:309px">Phone</div>
<div class="field" style="left:793px;top:2168px;width:307px">Message</div>
<div class="submit">SUBMIT</div>

<footer class="site-footer">
  <div class="foot-col" style="left:100px;width:116px">
    <h4>Quick Links</h4>
    <ul class="foot-links"><li>› <span style="color:#fff">Home</span></li><li>› About</li><li>› Gallery</li><li>› Equipment Hire</li><li>› Contact Us</li></ul>
  </div>
  <div class="foot-col" style="left:264px;width:225px">
    <h4>Contact Details</h4>
    <ul class="contact-list">
      <li><svg width="12" height="16" viewBox="0 0 12 16"><path d="M6 0a6 6 0 0 1 6 6c0 4-6 10-6 10S0 10 0 6a6 6 0 0 1 6-6z" fill="#ddd"/><circle cx="6" cy="6" r="2" fill="#242424"/></svg><span>48 Tidewater Lane, Harrowby Pk...<br>QLD 4217</span></li>
      <li><svg width="12" height="16" viewBox="0 0 12 16"><rect x="1" y="0" width="10" height="16" rx="2" fill="#ddd"/><rect x="3" y="2" width="6" height="10" fill="#242424"/></svg><span>0487 302 916</span></li>
      <li><svg width="14" height="14" viewBox="0 0 24 24"><path fill="#ddd" d="M6.6 10.8a15 15 0 0 0 6.6 6.6l2.2-2.2c.3-.3.7-.4 1-.2 1.1.4 2.3.6 3.6.6.6 0 1 .4 1 1V20c0 .6-.4 1-1 1A17 17 0 0 1 3 4c0-.6.4-1 1-1h3.5c.6 0 1 .4 1 1 0 1.3.2 2.5.6 3.6.1.3 0 .7-.2 1z"/></svg><span>0487 302 916</span></li>
      <li><svg width="14" height="12" viewBox="0 0 14 12"><rect width="14" height="12" fill="#ddd"/><path d="M0 0l7 6 7-6" stroke="#242424" fill="none"/></svg><span>info@brindlecoverestorations.com</span></li>
    </ul>
  </div>
  <div class="foot-col" style="left:532px;width:272px"><h4>Location Map</h4></div>
</footer>
<div class="map" role="img" aria-label="Street map showing the business location"></div>
<div class="copy-bar">
  <span class="copy-text">Copyright ©2016Brindlecoverestorations. All Rights Reserved.</span>
  <div class="social" style="left:962px;top:12px"><span class="social-dot s1"></span><span class="social-dot s2"></span><span class="social-dot s3"></span><span class="social-dot s4"></span></div>
</div>

</body>
</html>
```